Business card design needed for Automotive Reconditioning business

I have a logo design i just cant decide on the best color or layout for the business card, I will upload all the files so you can see all colors schemes we are considering. I have other file formats if needed let me know.

Target Market(s)

automotive dealerships

Contact Information for Business Card

HERE are the Descriptions and info needed on the card:
Interior Repair: Leather carpet burns panels dash Deoderize
Dealer products and Vin Verify
( spot for name and cell number) My name is Norman Bexley phone 614 352-4180 Title COO www.QuorvalMotive.com

Font styles to use
Sans Serif
Other font styles liked:
• what ever you think looks best

Requirements
Must have
• Must be able to change the name and phone for employees

```html
<!DOCTYPE html>
<html lang="en">
<head>
<meta charset="utf-8">
<title>Quorval Motive – Business Card</title>
<link rel="stylesheet" href="https://fonts.googleapis.com/css2?family=Montserrat:wght@300;400;600;700;800&display=swap">
<style>
  :root {
    --page-bg: #e8e9ea;
    --card-bg: #2c2b2c;
    --card-bg-dark: #1f1e1f;
    --brand-red: #d8402b;
    --brand-red-dark: #a92a1c;
    --brand-red-light: #e2543c;
    --brand-red-edge: #f07a63;
    --brand-blue: #4a7fd0;
    --text-light: #ffffff;
    --text-soft: #e4e4e4;
  }
  * { margin: 0; padding: 0; box-sizing: border-box; }
  html, body {
    width: 1200px;
    height: 969px;
    overflow: hidden;
    background: var(--page-bg);
    font-family: "Montserrat", sans-serif;
  }
  .canvas {
    position: relative;
    width: 1200px;
    height: 969px;
    display: flex;
    align-items: center;
    justify-content: center;
  }
  .business-card {
    position: relative;
    width: 1000px;
    height: 572px;
    background: linear-gradient(135deg, var(--card-bg) 0%, var(--card-bg-dark) 100%);
    border-radius: 6px;
    overflow: hidden;
    box-shadow: 0 18px 40px rgba(0,0,0,0.18);
  }
  .flag-panel {
    position: absolute;
    inset: 0;
    width: 100%;
    height: 100%;
  }
  .brand-name {
    position: absolute;
    left: 86px;
    top: 110px;
    width: 540px;
    color: var(--brand-red);
    font-weight: 800;
    text-transform: uppercase;
    line-height: 1.05;
    white-space: nowrap;
  }
  .brand-name .brand-main { display: block; font-size: 46px; letter-spacing: 1px; }
  .brand-name .brand-sub { display: block; font-size: 22px; letter-spacing: 1.5px; margin-top: 12px; }
  .services {
    position: absolute;
    left: 640px;
    top: 78px;
    width: 330px;
    list-style: none;
  }
  .service {
    display: flex;
    align-items: flex-start;
    gap: 18px;
    margin-bottom: 38px;
  }
  .service-icon {
    flex: none;
    width: 62px;
    height: 62px;
    border-radius: 10px;
    background: linear-gradient(180deg, var(--brand-red) 0%, var(--brand-red-dark) 100%);
    border: 2px solid #f06a55;
  }
  .service-text {
    color: var(--text-soft);
    font-size: 16px;
    line-height: 1.4;
    padding-top: 2px;
  }
  .service-text strong { color: var(--text-light); font-weight: 700; display: block; }
  .name-block {
    position: absolute;
    left: 118px;
    top: 318px;
  }
  .title-tab {
    position: absolute;
    z-index: 0;
    left: 478px;
    top: -26px;
    width: 185px;
    height: 46px;
    background: var(--brand-blue);
    transform: skewX(-12deg);
    display: flex;
    align-items: center;
    justify-content: center;
    padding-left: 18px;
    color: var(--text-light);
    font-size: 26px;
    font-weight: 400;
    letter-spacing: 2px;
  }
  .title-tab span { transform: skewX(12deg); }
  .name-badge {
    position: relative;
    z-index: 1;
    width: 500px;
    height: 100px;
    border-radius: 10px;
    background: linear-gradient(180deg, var(--brand-red-light) 0%, var(--brand-red-dark) 100%);
    border: 3px solid var(--brand-red-edge);
    display: flex;
    align-items: center;
    padding: 0 26px;
    color: var(--text-light);
    font-size: 40px;
    text-transform: uppercase;
    letter-spacing: 1px;
    white-space: nowrap;
    overflow: hidden;
  }
  .name-badge .first-name { font-weight: 700; }
  .name-badge .last-name { font-weight: 300; margin-left: 12px; }
  .contact-row {
    position: absolute;
    left: 110px;
    top: 470px;
    display: flex;
    gap: 70px;
    color: var(--text-light);
    font-size: 34px;
    font-weight: 400;
    white-space: nowrap;
  }
  .contact-item { display: flex; align-items: center; gap: 16px; }
  .contact-icon { width: 40px; height: 40px; flex: none; }
</style>
</head>
<body>
<main class="canvas">
  <article class="business-card">
    <svg class="flag-panel" viewBox="0 0 1000 572" preserveAspectRatio="none" role="img" aria-label="Checkered racing flag pattern along the left edge">
      <defs>
        <linearGradient id="flagTone" x1="0" y1="0" x2="1" y2="1">
          <stop offset="0" stop-color="#d9d9d9"/>
          <stop offset="1" stop-color="#6d6d6d"/>
        </linearGradient>
      </defs>
      <polygon points="0,0 250,0 70,572 0,572" fill="url(#flagTone)"/>
    </svg>

    <h1 class="brand-name">
      <span class="brand-main">Quorval Motive</span>
      <span class="brand-sub">Auto Reconditioning Corp.</span>
    </h1>

    <ul class="services">
      <li class="service">
        <span class="service-icon" role="img" aria-label="Car seat icon"></span>
        <p class="service-text"><strong>Interior Repair:</strong>Leather Carpet Burns<br>Panels Dash Deoderize</p>
      </li>
      <li class="service">
        <span class="service-icon" role="img" aria-label="Gear shifter icon"></span>
        <p class="service-text">Dealer products &amp;<br>Vin Verify</p>
      </li>
    </ul>

    <div class="name-block">
      <div class="title-tab"><span>COO</span></div>
      <div class="name-badge">
        <span class="first-name">Norman</span><span class="last-name">Bexley</span>
      </div>
    </div>

    <div class="contact-row">
      <div class="contact-item contact-phone">
        <svg class="contact-icon" viewBox="0 0 40 40" aria-hidden="true">
          <circle cx="20" cy="20" r="18" fill="none" stroke="#fff" stroke-width="2.5"/>
          <path d="M14 11c1-1 2.5-1 3 .3l1.6 3.4c.4.9 0 1.7-.7 2.2l-1.3 1c1 2.4 2.8 4.3 5.2 5.3l1-1.3c.5-.7 1.4-1 2.2-.6l3.4 1.6c1.2.6 1.2 2 .3 3l-1.5 1.5c-1.3 1.3-3.6 1.4-6-.1-3.4-2-6-4.7-7.9-8-1.4-2.4-1.3-4.7 0-6z" fill="#fff"/>
        </svg>
        <span>614 352-4180</span>
      </div>
      <div class="contact-item contact-web">
        <svg class="contact-icon" viewBox="0 0 40 40" aria-hidden="true">
          <circle cx="20" cy="20" r="18" fill="none" stroke="#fff" stroke-width="2.5"/>
          <path d="M14 11c1-1 2.5-1 3 .3l1.6 3.4c.4.9 0 1.7-.7 2.2l-1.3 1c1 2.4 2.8 4.3 5.2 5.3l1-1.3c.5-.7 1.4-1 2.2-.6l3.4 1.6c1.2.6 1.2 2 .3 3l-1.5 1.5c-1.3 1.3-3.6 1.4-6-.1-3.4-2-6-4.7-7.9-8-1.4-2.4-1.3-4.7 0-6z" fill="#fff"/>
        </svg>
        <span>QuorvalMotive.com</span>
      </div>
    </div>
  </article>
</main>
</body>
</html>
```